Harmony Swift Care Business card

We want a business card that matches our business theme. Our website is www.swiftcarehub.example
The company name is Harmony Swift Care
The persons having the business cards will be doctors
My logo is attached.
We have a drive-thru medical center where our motto is Fast, Reliable, and Convenient. Our goal is to change the medical space while utilizing technologies, keeping a professional and clean look

Medical

Info on the card should be: Name, Position, Cell number, website, email address, possibly the office line as well

Requirements
Must have
• Logo
Nice to have
• Professional medical feel with our logo colors incorporated

```html
<!DOCTYPE html>
<html lang="en">
<head>
<meta charset="utf-8">
<title>Harmony Swift Care – Business Card</title>
<link rel="stylesheet" href="https://fonts.googleapis.com/css2?family=Lato:wght@400;700;900&family=Raleway:wght@500&display=swap">
<style>
  :root {
    --navy: #1b4a9f;
    --sky: #3fc8f2;
    --faint: #e9eef7;
    --ink: #1d1d1f;
    --paper: #ffffff;
  }
  * { margin: 0; padding: 0; box-sizing: border-box; }
  html, body { width: 685px; height: 1200px; overflow: hidden; background: var(--paper); }
  body { position: relative; font-family: 'Lato', Arial, sans-serif; }

  .backdrop { position: absolute; inset: 0; }

  .card {
    position: absolute; left: 70px; width: 544px; height: 311px;
    background: var(--paper); overflow: hidden;
    box-shadow: 0 2px 8px rgba(0,0,0,0.12);
  }
  .card--front { top: 300px; }
  .card--back { top: 648px; }

  .card__emblem {
    position: absolute; right: -96px; top: 14px; width: 258px; height: 258px;
    border-radius: 50%; background: var(--faint);
  }
  .card__band { position: absolute; left: 0; bottom: 0; width: 100%; height: 19px; display: flex; }
  .card__band span:first-child { flex: 1; background: var(--sky); }
  .card__band span:last-child { flex: 1; background: var(--navy); }

  .brand { position: absolute; display: flex; align-items: center; }
  .brand__dot { border-radius: 50%; background: var(--navy); flex: none; }
  .brand__name { font-weight: 900; color: var(--navy); line-height: 1; white-space: nowrap; }

  .card--front .brand { left: 52px; top: 42px; gap: 12px; }
  .card--front .brand__dot { width: 44px; height: 44px; }
  .card--front .brand__name { font-size: 26px; }

  .card--back .brand { left: 56px; top: 120px; gap: 14px; }
  .card--back .brand__dot { width: 54px; height: 54px; }
  .card--back .brand__name { font-size: 32px; }

  .holder { position: absolute; left: 0; top: 138px; width: 100%; text-align: center; }
  .holder__name { font-weight: 900; font-size: 20px; color: var(--navy); line-height: 24px; }
  .holder__role { font-family: 'Raleway', Arial, sans-serif; font-weight: 500; font-size: 14px; color: var(--navy); line-height: 18px; }
  .rule { position: absolute; top: 162px; height: 2px; background: var(--navy); }
  .rule--left { left: 0; width: 170px; }
  .rule--right { right: 0; width: 170px; }

  .contacts { position: absolute; top: 198px; list-style: none; }
  .contacts--left { left: 44px; }
  .contacts--right { left: 266px; }
  .contacts li { display: flex; align-items: center; height: 28px; font-size: 15.5px; color: var(--navy); white-space: nowrap; }
  .contacts li.indent { padding-left: 31px; }
  .icon { width: 18px; height: 18px; margin-right: 13px; flex: none; }
</style>
</head>
<body>
  <svg class="backdrop" width="685" height="1200" viewBox="0 0 685 1200" aria-hidden="true">
    <polygon points="685,488 685,1200 0,1200" fill="var(--navy)"/>
  </svg>

  <section class="card card--front" aria-label="Business card front">
    <div class="card__emblem" aria-hidden="true"></div>
    <div class="brand">
      <span class="brand__dot" aria-hidden="true"></span>
      <span class="brand__name">Harmony Swift Care</span>
    </div>

    <span class="rule rule--left"></span>
    <span class="rule rule--right"></span>
    <div class="holder">
      <h1 class="holder__name">DR. ALAN MERCER</h1>
      <p class="holder__role">Professional Surgeon</p>
    </div>

    <ul class="contacts contacts--left">
      <li>
        <svg class="icon" viewBox="0 0 18 18"><rect width="18" height="18" fill="var(--navy)"/><rect x="6" y="3" width="7" height="12" rx="1" fill="none" stroke="#fff" stroke-width="1.4"/><rect x="8.5" y="12.5" width="2" height="1" fill="#fff"/></svg>
        +000 5550 1942
      </li>
      <li>
        <svg class="icon" viewBox="0 0 18 18"><rect width="18" height="18" fill="var(--navy)"/><path d="M5 4 L7.5 4 L8.5 7 L7 8.2 Q8.5 10.8 10.8 12 L12 10.5 L15 11.5 L15 14 Q9 15 4 8 Z" fill="#fff"/></svg>
        +000 5550 1942
      </li>
      <li>
        <svg class="icon" viewBox="0 0 18 18"><rect width="18" height="18" fill="var(--navy)"/><rect x="3" y="5" width="12" height="8.5" fill="none" stroke="#fff" stroke-width="1.2"/><path d="M3 5 L9 10 L15 5" fill="none" stroke="#fff" stroke-width="1.2"/></svg>
        a.mercer@swiftcare.example
      </li>
    </ul>

    <ul class="contacts contacts--right">
      <li>
        <svg class="icon" viewBox="0 0 18 18"><rect width="18" height="18" fill="var(--navy)"/><circle cx="9" cy="9" r="5.5" fill="none" stroke="#fff" stroke-width="1.2"/><path d="M3.5 9 H14.5 M9 3.5 V14.5" stroke="#fff" stroke-width="1"/><ellipse cx="9" cy="9" rx="2.5" ry="5.5" fill="none" stroke="#fff" stroke-width="1"/></svg>
        www.swiftcarehub.example
      </li>
      <li>
        <svg class="icon" viewBox="0 0 18 18"><rect width="18" height="18" fill="var(--navy)"/><path d="M9 15 Q4.5 9.5 4.5 7.5 A4.5 4.5 0 0 1 13.5 7.5 Q13.5 9.5 9 15 Z" fill="#fff"/><circle cx="9" cy="7.5" r="1.7" fill="var(--navy)"/></svg>
        Harbor Lane, Unit 7
      </li>
      <li class="indent">Westfield Road, Care Centre</li>
    </ul>

    <div class="card__band" aria-hidden="true"><span></span><span></span></div>
  </section>

  <section class="card card--back" aria-label="Business card back">
    <div class="card__emblem" aria-hidden="true"></div>
    <div class="brand">
      <span class="brand__dot" aria-hidden="true"></span>
      <span class="brand__name">Harmony Swift Care</span>
    </div>
    <div class="card__band" aria-hidden="true"><span></span><span></span></div>
  </section>
</body>
</html>
```